Redesign the Eshop of a gift shop

We want to redesign the front page, the category page and the product page of our Eshop that sells gifts.
I am thinking not to reveal the url of the eshop as i don't want you to get influenced. Lets call the Eshop "PresentNest.com"
I will list the brands that we resell so you understand what we are selling,
Morvato-https://www.morvato-example.com/
Zandorpel-https://zandorpel-example.com/
Vamtol - https://vamtol-example.com/
Quiet Orchard - https://www.quietorchard-example.com/
Ranger's Workbench - https://rangersworkbench-example.com/
Plumeline press - https://plumelinepress-example.com/
Tarpawn - https://tarpawnofficial-example.com/
We also sell toys for adults like backgamon, chess, playing cards, board games.
The problem is that many eshops sell these and thats why i would like the design to have a different approach, more fresh, not seen before.
I am also thinking of something playfull, happy, but warm at the same time.
Please note that our logo is black & white but feel free to play with any color/s you like in your website design. We might eventually even adjust the logo colors, or you can provide a pallete that suites a black and white logo
Let me know if you have any questions!
Updates
A couple of designers kindly asked to extend so they can submit.
Target Market(s)
Age: 20-50, Gender: Also men but mostly women, Income: Moderate to high, Interests and Lifestyle: Customers who value sentimentality, personal connection, and thoughtful gestures, Relationship Status: Those in relationships or with larger families
Number of Pages Required
3 page
Look and feel
Each slider illustrates characteristics of the customer's brand and the style your logo design should communicate.

```html
<!DOCTYPE html>
<html lang="en">
<head>
<meta charset="utf-8">
<title>PresentNest.com – Gift Shop</title>
<link href="https://fonts.googleapis.com/css2?family=Rubik:wght@300;400;500;600;700&display=swap" rel="stylesheet">
<style>
:root{
  --ink:#161616;
  --ink-soft:#444;
  --muted:#666;
  --paper:#ffffff;
  --sun:#f9ef9f;
  --dark:#1d1d1d;
  --night:#050505;
  --gold:#f5a623;
  --line:#d9d9d9;
}
*{margin:0;padding:0;box-sizing:border-box}
html,body{width:1200px;height:4078px;overflow:hidden}
body{position:relative;font-family:'Rubik',sans-serif;color:var(--ink);background:var(--paper)}
.abs{position:absolute}
.sun-band{position:absolute;left:0;top:692px;width:1200px;height:3021px;background:var(--sun)}
.night-band{position:absolute;left:0;top:3713px;width:1200px;height:365px;background:var(--night)}

/* header */
.brand{position:absolute;display:flex;align-items:center;gap:7px;font-weight:400;font-size:20px;line-height:1;white-space:nowrap}
.brand .mark{width:14px;height:14px;background:currentColor;flex:none}
.nav{position:absolute;top:45px;left:265px;font-size:15px;color:var(--ink-soft)}
.nav a{color:inherit;text-decoration:none;position:absolute;white-space:nowrap}
.nav a.active{color:var(--ink);font-weight:500}
.tools svg{position:absolute}

/* hero */
.eyebrow{left:94px;top:190px;font-size:21px;font-weight:300}
.hero-title{left:94px;top:222px;font-size:43px;font-weight:600;line-height:56px}
.hero-copy{left:94px;top:349px;font-size:13px;line-height:18px;color:var(--ink-soft);width:380px}
.btn{position:absolute;background:var(--dark);color:#fff;font-size:12px;font-weight:600;display:flex;align-items:center;justify-content:center;border-radius:7px;box-shadow:0 8px 18px rgba(120,90,20,.35);text-transform:uppercase;white-space:nowrap}
.media{position:absolute;border-radius:4px}

/* search */
.finder{left:128px;top:600px;width:950px;height:167px;background:#fff;border-radius:0 0 12px 12px}
.finder h2{position:absolute;left:70px;top:45px;font-size:27px;font-weight:500;white-space:nowrap}
.finder .icon{position:absolute;left:30px;top:52px;width:22px;height:20px;background:var(--ink)}
.finder label{position:absolute;top:32px;font-size:13px;white-space:nowrap}
.select{position:absolute;top:63px;width:190px;height:37px;border:1px solid var(--line);border-radius:6px;font-size:11px;color:#777;padding:12px 10px}
.select::after{content:"";position:absolute;right:12px;top:14px;width:6px;height:6px;border-right:1px solid #999;border-bottom:1px solid #999;transform:rotate(45deg)}

/* promo tiles */
.tile{position:absolute;top:869px;width:237px;height:207px;border-radius:4px;color:#fff;font-weight:700;font-size:16px;text-transform:uppercase}
.tile span{position:absolute;left:0;right:0;bottom:22px;text-align:center}

.section-title{position:absolute;left:0;width:1200px;text-align:center;font-size:33px;font-weight:500}
.tab{position:absolute;top:1227px;width:138px;height:39px;border:1px solid #8a8060;border-radius:6px;font-size:11px;display:flex;align-items:center;justify-content:center}
.tab.on{background:var(--night);color:#fff;font-weight:600;border-color:var(--night)}

.product{position:absolute;top:1372px;width:228px;height:363px;background:#fff;border-radius:4px;overflow:hidden}
.product .pic{height:181px}
.product h3{position:absolute;left:20px;top:207px;width:140px;font-size:12px;font-weight:600;line-height:16px}
.product .heart{position:absolute;right:26px;top:210px}
.product .range{position:absolute;left:20px;font-size:12px}
.product .buy{position:absolute;left:20px;top:294px;width:110px;height:39px;border:2px solid var(--ink);border-radius:7px;font-size:13px;font-weight:600;display:flex;align-items:center;justify-content:center}
.product .price{position:absolute;right:22px;top:306px;font-size:12px;font-weight:600}

.category{position:absolute;width:314px;height:458px}
.cat-label{position:absolute;font-size:17px;font-weight:600;text-align:center;width:314px}

.perk{position:absolute;top:2798px;width:245px;height:292px;background:#fff;border-radius:22px}
.perk svg{position:absolute;left:24px;top:44px}
.perk h3{position:absolute;left:24px;top:126px;font-size:17px;font-weight:600;white-space:nowrap}
.perk p{position:absolute;left:24px;width:200px;font-size:12px;line-height:19px;color:var(--muted)}

.photo{position:absolute;box-shadow:0 6px 16px rgba(0,0,0,.25)}
.quote{left:706px;top:3302px;width:350px;font-size:14px;line-height:19px;color:var(--ink-soft)}
.star{position:absolute;top:3252px}

.letter{left:125px;top:3617px;width:949px;height:188px;background:#fff;border-radius:10px}
.letter h2{position:absolute;left:50px;top:50px;font-size:27px;font-weight:500}
.letter p{position:absolute;left:50px;top:98px;width:540px;font-size:13px;line-height:21px;color:var(--ink-soft)}

.foot-brand{position:absolute;left:0;top:3868px;width:1200px;display:flex;justify-content:center}
.foot-brand .brand{position:static;color:#fff;font-size:28px}
.foot-brand .brand .mark{width:18px;height:18px}
.foot-links{position:absolute;top:3929px;left:0;width:1200px;display:flex;justify-content:center;gap:44px;color:#fff;font-size:16px;font-weight:600}
.social{position:absolute;top:3975px;width:27px;height:27px;border:3px solid #fff;border-radius:5px}
.rule{left:89px;top:4036px;width:1022px;height:1px;background:#777}
.copy{left:0;top:4050px;width:1200px;text-align:center;color:#fff;font-size:14px;font-weight:600}
</style>
</head>
<body>

<div class="sun-band"></div>
<div class="night-band"></div>

<!-- header -->
<header>
  <div class="brand" style="left:97px;top:45px"><span class="mark"></span>PresentNest</div>
  <nav class="nav">
    <a class="active" style="left:0">Home</a>
    <a style="left:93px">Category</a>
    <a style="left:210px">Products</a>
    <a style="left:327px">Services</a>
    <a style="left:440px">Contact</a>
  </nav>
  <div class="tools">
    <svg style="left:938px;top:43px" width="22" height="20" viewBox="0 0 22 20" fill="none" stroke="#161616" stroke-width="1.6"><path d="M1 2h4l3 11h11l2-8H6"/><circle cx="9" cy="17" r="1.4"/><circle cx="18" cy="17" r="1.4"/></svg>
    <svg style="left:994px;top:41px" width="20" height="22" viewBox="0 0 20 22" fill="none" stroke="#161616" stroke-width="1.6"><circle cx="10" cy="7" r="5"/><path d="M1 21c1-5 5-7 9-7s8 2 9 7"/></svg>
    <div class="abs" style="left:1051px;top:43px;width:1px;height:22px;background:#161616"></div>
    <svg style="left:1088px;top:46px" width="20" height="14" viewBox="0 0 20 14" stroke="#161616" stroke-width="1.6"><path d="M0 1h20M4 7h16M0 13h20"/></svg>
  </div>
</header>

<!-- hero -->
<section>
  <p class="abs eyebrow">The Best Gift Shop</p>
  <h1 class="abs hero-title">Creating Happiness<br>For your loved Ones</h1>
  <p class="abs hero-copy">Lorem ipsum dolor sit amet, consectetur adipiscing elit.<br>Sed sit amet justo ipsum.</p>
  <div class="btn" style="left:94px;top:434px;width:134px;height:40px">Choose a gift</div>
  <div class="media" role="img" aria-label="Stack of black, gold and silver wrapped gift boxes with confetti" style="left:470px;top:180px;width:630px;height:330px;background:radial-gradient(ellipse at 50% 60%,#6b6252 0%,#2a2824 45%,rgba(255,255,255,0) 72%)"></div>
</section>

<!-- gift finder -->
<section class="abs finder">
  <span class="icon"></span>
  <h2>Need A Gift Now?</h2>
  <label style="left:356px">Where is it going?</label>
  <div class="select" style="left:356px">Select Destination</div>
  <label style="left:568px">When should it get there?</label>
  <div class="select" style="left:568px">Select delivery date</div>
  <div class="btn" style="left:779px;top:60px;width:133px;height:38px">Find a gift</div>
</section>

<!-- promo tiles -->
<section>
  <div class="tile" role="img" aria-label="Dark leather wallets" style="left:103px;background:linear-gradient(135deg,#3a3d36,#1c1e1a)">
    <span style="top:75px;bottom:auto;font-size:16px">Special offer</span>
    <span style="top:96px;bottom:auto;font-size:31px">25% off</span>
  </div>
  <div class="tile" role="img" aria-label="Notebook with pens on a desk" style="left:353px;background:linear-gradient(135deg,#b9b6ac,#d6a98a)"><span>Birthday gift</span></div>
  <div class="tile" role="img" aria-label="Engraved wooden keepsake box" style="left:606px;background:linear-gradient(135deg,#7a6a5a,#5a3a26)"><span>Anniversary gift</span></div>
  <div class="tile" role="img" aria-label="Gift box with candle and cards" style="left:858px;background:linear-gradient(135deg,#d8c7ae,#b59b7c)"><span>Love gifts</span></div>
</section>

<!-- popular -->
<h2 class="section-title" style="top:1144px">Popular Gift Collections</h2>
<div class="tab on" style="left:294px">New Gifts</div>
<div class="tab" style="left:443px">Top Rated Gifts</div>
<div class="tab" style="left:591px">Trending Gifts</div>
<div class="tab" style="left:739px">Best Offer Gifts</div>

<article class="product" style="left:103px">
  <div class="pic" role="img" aria-label="Pastel backpack" style="background:linear-gradient(180deg,#eeeeee,#e0d8d4)"></div>
  <h3>Macaroon Tarpawn X Nyrolu Series</h3>
  <svg class="heart" width="22" height="20" viewBox="0 0 22 20" fill="none" stroke="#555" stroke-width="1.3"><path d="M11 18S1 12 1 6a5 5 0 0 1 10-1 5 5 0 0 1 10 1c0 6-10 12-10 12z"/></svg>
  <p class="range" style="top:254px">$548.00-$740.00</p>
  <div class="buy">GIFT NOW</div><p class="price">$657</p>
</article>
<article class="product" style="left:358px">
  <div class="pic" role="img" aria-label="Patterned pink journal" style="background:linear-gradient(135deg,#c98a78,#e9d6cf)"></div>
  <h3>Guided Wellness Journal</h3>
  <svg class="heart" width="22" height="20" viewBox="0 0 22 20" fill="none" stroke="#555" stroke-width="1.3"><path d="M11 18S1 12 1 6a5 5 0 0 1 10-1 5 5 0 0 1 10 1c0 6-10 12-10 12z"/></svg>
  <p class="range" style="top:254px">$548.00-$740.00</p>
  <div class="buy">GIFT NOW</div><p class="price">$26</p>
</article>
<article class="product" style="left:612px">
  <div class="pic" role="img" aria-label="Puzzle tube with coastal scene" style="background:linear-gradient(180deg,#f7f7f7,#e8c9a0)"></div>
  <h3>Halvers Group 500 Piece Jigsaw ...</h3>
  <svg class="heart" width="22" height="20" viewBox="0 0 22 20" fill="none" stroke="#555" stroke-width="1.3"><path d="M11 18S1 12 1 6a5 5 0 0 1 10-1 5 5 0 0 1 10 1c0 6-10 12-10 12z"/></svg>
  <p class="range" style="top:263px">$548.00-$740.00</p>
  <div class="buy">GIFT NOW</div><p class="price">$24</p>
</article>
<article class="product" style="left:867px">
  <div class="pic" role="img" aria-label="Amber fragrance bottle" style="background:linear-gradient(135deg,#7a4a14,#c9c0b8)"></div>
  <h3>Natural Fragrance Cologne</h3>
  <svg class="heart" width="22" height="20" viewBox="0 0 22 20" fill="none" stroke="#555" stroke-width="1.3"><path d="M11 18S1 12 1 6a5 5 0 0 1 10-1 5 5 0 0 1 10 1c0 6-10 12-10 12z"/></svg>
  <p class="range" style="top:254px">$548.00-$740.00</p>
  <div class="buy">GIFT NOW</div><p class="price">$40</p>
</article>
<div class="btn" style="left:533px;top:1777px;width:133px;height:40px">View all</div>

<!-- categories -->
<h2 class="section-title" style="top:1905px">Cateogires</h2>
<div class="category" role="img" aria-label="Brown leather wallet" style="left:103px;top:1980px;border-radius:30px 70px 0 30px;background:linear-gradient(135deg,#4a3a30,#8a4a26 60%,#2a1f1a)"></div>
<p class="cat-label" style="left:103px;top:2455px">WALLET</p>
<div class="category" role="img" aria-label="Colourful clothes on a rail" style="left:443px;top:2024px;border-radius:70px 70px 30px 30px;background:linear-gradient(90deg,#4a4f45,#d9692e 40%,#7a8fa3 65%,#c23a2a)"></div>
<p class="cat-label" style="left:443px;top:2500px">CLOTHING</p>
<div class="category" role="img" aria-label="Kraft spiral notebooks" style="left:781px;top:1980px;border-radius:70px 30px 30px 0;background:linear-gradient(135deg,#e6e6ec,#a47c54 40%,#8f6a45)"></div>
<p class="cat-label" style="left:781px;top:2455px">STATIONARY</p>
<div class="btn" style="left:533px;top:2561px;width:133px;height:39px">View all</div>

<!-- deliver -->
<h2 class="section-title" style="top:2688px">We Deliver Happiness</h2>
<p class="abs" style="left:0;top:2740px;width:1200px;text-align:center;font-size:13px;color:var(--ink-soft)">Lorem ipsum dolor sit amet, consectetur adipiscing elit.Sed sit amet justo ipsum.</p>

<div class="perk" style="left:89px">
  <svg width="50" height="50" viewBox="0 0 50 50" fill="none" stroke="#161616" stroke-width="1.6"><rect x="6" y="30" width="38" height="16"/><rect x="10" y="20" width="30" height="10"/><path d="M17 12v8M25 10v10M33 12v8M3 46h44"/></svg>
  <h3>BIRTHDAY GIFT'S</h3>
  <p style="top:160px">Lorem Ipsum is simply dummy text of the printing and typesetting industry. Lorem Ipsum has been the industry's standard dummy text ever since the 1500s.</p>
</div>
<div class="perk" style="left:347px">
  <svg width="56" height="50" viewBox="0 0 56 50" fill="none" stroke="#161616" stroke-width="1.6"><circle cx="20" cy="30" r="14"/><circle cx="36" cy="30" r="14"/><path d="M16 12l4-5 4 5"/></svg>
  <h3>ANNIVERSARY GIFT'S</h3>
  <p style="top:160px">Lorem Ipsum is simply dummy text of the printing and typesetting industry. Lorem Ipsum has been the industry's standard dummy text ever since the 1500s.</p>
</div>
<div class="perk" style="left:607px">
  <svg width="50" height="50" viewBox="0 0 50 50" fill="none" stroke="#161616" stroke-width="1.6"><rect x="4" y="18" width="42" height="9"/><rect x="8" y="27" width="34" height="20"/><path d="M25 18v29M25 18c-6-10-14-6-10 0M25 18c6-10 14-6 10 0"/></svg>
  <h3>SPECIAL GIFTS</h3>
  <p style="top:170px">Lorem Ipsum is simply dummy text of the printing and typesetting industry. Lorem Ipsum has been the industry's standard dummy text ever since the 1500s.</p>
</div>
<div class="perk" style="left:866px">
  <svg width="56" height="50" viewBox="0 0 56 50" fill="none" stroke="#161616" stroke-width="1.6"><rect x="6" y="26" width="34" height="21"/><rect x="4" y="20" width="38" height="6"/><path d="M23 20v27M44 18s-8-5-8-10a4 4 0 0 1 8-1 4 4 0 0 1 8 1c0 5-8 10-8 10z"/></svg>
  <h3>LOVE GIFTS</h3>
  <p style="top:160px">Lorem Ipsum is simply dummy text of the printing and typesetting industry. Lorem Ipsum has been the industry's standard dummy text ever since the 1500s.</p>
</div>

<!-- feedback -->
<h2 class="abs" style="left:103px;top:3168px;font-size:33px;font-weight:500">Customer Feedback</h2>
<div class="photo" role="img" aria-label="Customer portrait" style="left:111px;top:3312px;width:119px;height:156px;background:linear-gradient(160deg,#8a8f90,#c9b9ad)"></div>
<div class="photo" role="img" aria-label="Customer portrait" style="left:262px;top:3285px;width:163px;height:205px;background:linear-gradient(160deg,#3b3b36,#9a7a6a)"></div>
<div class="photo" role="img" aria-label="Customer portrait" style="left:459px;top:3242px;width:219px;height:270px;background:linear-gradient(160deg,#6a7a8a,#5a2a26 60%,#c6a48a)"></div>

<svg class="star" style="left:706px" width="210" height="30" viewBox="0 0 210 30" fill="#f5a623">
  <defs><path id="s" d="M15 1l4 9 10 1-7.5 7 2 10L15 23l-8.5 5 2-10L1 11l10-1z"/></defs>
  <use href="#s"/><use href="#s" x="43"/><use href="#s" x="86"/><use href="#s" x="129"/><use href="#s" x="172"/>
</svg>
<p class="abs quote">Lorem Ipsum is simply dummy text of the printing and typesetting industry. Lorem Ipsum has been the industry's standard dummy text ever since the 1500s, when an unknown printer took a galley of type and scrambled it to make a type specimen book. It has survived not only five centuries, but also the leap into electronic typesetting, remaining essentially unchanged.</p>
<p class="abs" style="left:706px;top:3474px;font-size:17px;font-weight:600">Maren Ostby</p>

<!-- newsletter -->
<section class="abs letter">
  <h2>Want more special gifts ideas?</h2>
  <p>Lorem Ipsum is simply dummy text of the printing and typesetting industry. Lorem Ipsum has been the industry's standard dummy text ever since the 1500s,</p>
  <div class="btn" style="left:637px;top:76px;width:262px;height:37px;font-size:13px">Subscribe to our newsletter</div>
</section>

<!-- footer -->
<footer>
  <div class="foot-brand"><div class="brand"><span class="mark"></span>PresentNest</div></div>
  <nav class="foot-links"><span>Home</span><span>Category</span><span>Products</span><span>Services</span><span>Contact</span></nav>
  <span class="social" aria-label="Social link" style="left:522px"></span>
  <span class="social" aria-label="Social link" style="left:565px"></span>
  <span class="social" aria-label="Social link" style="left:607px"></span>
  <span class="social" aria-label="Social link" style="left:650px"></span>
  <div class="abs rule"></div>
  <p class="abs copy">© 2023 Orrin. All rights reserved</p>
</footer>

</body>
</html>
```